Looking for a cool & simple business-card-design for digital agency

Hi!

We are a web agency that offers Reputation Management, Zorvik & Seo Services and software development. We like cool things, we like innovative styles.

We have uploaded our logo.

Project Deadline Extended Reason: Client does not want any designs with the colorful logo. Please send us submissions ONLY with the blac and white logo. What the client would like to see:1) Back of the card: is a silver logo on a black background2) front of the card with all the data, please use white background and black logo thank you Added Friday, May 8, 2015

Software

```html
<!DOCTYPE html>
<html lang="de">
<head>
<meta charset="utf-8">
<title>Lumora AG – Visitenkarte</title>
<link rel="stylesheet" href="https://fonts.googleapis.com/css2?family=Source+Sans+3:wght@400;600;700&family=Exo+2:wght@300&display=swap">
<style>
  :root {
    --backdrop: #8d8f91;
    --card-black: #141213;
    --card-white: #f3f3f1;
    --silver: #e4e4e2;
    --ink: #151515;
    --ink-soft: #2a2a2a;
  }
  * { box-sizing: border-box; margin: 0; padding: 0; }
  html, body {
    width: 1200px; height: 1200px; overflow: hidden;
    background: var(--backdrop);
  }
  .stage {
    position: relative; width: 1200px; height: 1200px;
    display: flex; flex-direction: column; align-items: center; justify-content: center; gap: 60px;
  }
  .card {
    position: relative; width: 700px; height: 400px;
    box-shadow: 0 6px 18px rgba(0,0,0,.25);
    font-family: "Source Sans 3", sans-serif;
  }
  /* Back */
  .card-back { background: var(--card-black); color: var(--silver); }
  .card-back .brand {
    position: absolute; right: 60px; top: 150px; text-align: left;
  }
  .brand-row { display: flex; align-items: center; gap: 14px; }
  .brand-dot { width: 22px; height: 22px; border-radius: 50%; background: currentColor; }
  .brand-name {
    font-family: "Source Sans 3", sans-serif; font-weight: 700;
    line-height: 1;
  }
  .card-back .brand-name { font-size: 64px; }
  .tagline {
    font-family: "Exo 2", sans-serif; font-weight: 300;
    text-transform: uppercase; letter-spacing: .32em;
  }
  .card-back .tagline { font-size: 21px; margin-top: 8px; margin-left: 36px; }

  /* Front */
  .card-front { background: var(--card-white); color: var(--ink); }
  .card-front .brand { position: absolute; right: 40px; top: 36px; }
  .card-front .brand-dot { width: 14px; height: 14px; }
  .card-front .brand-name { font-size: 36px; }
  .card-front .tagline { font-size: 14px; margin-top: 4px; margin-left: 28px; }
  .address {
    position: absolute; right: 40px; top: 128px; text-align: right;
    font-size: 20px; line-height: 1.3; color: var(--ink-soft);
  }
  .address .with-icon { display: inline-flex; align-items: center; gap: 8px; }
  .person { position: absolute; left: 52px; top: 118px; }
  .person-name { font-size: 22px; font-weight: 700; letter-spacing: .01em; }
  .person-title { font-size: 18px; color: var(--ink-soft); margin-top: 2px; }
  .contacts { list-style: none; margin-top: 16px; }
  .contacts li {
    display: flex; align-items: center; gap: 10px;
    font-size: 19px; line-height: 1.35; color: var(--ink-soft);
  }
  .icon { width: 16px; height: 16px; flex: none; fill: var(--ink); }
</style>
</head>
<body>
<main class="stage">
  <section class="card card-back" aria-label="Kartenrückseite">
    <div class="brand">
      <div class="brand-row"><span class="brand-dot"></span><span class="brand-name">Lumora AG</span></div>
      <div class="tagline">Digitale Strategien</div>
    </div>
  </section>

  <section class="card card-front" aria-label="Kartenvorderseite">
    <div class="brand">
      <div class="brand-row"><span class="brand-dot"></span><span class="brand-name">Lumora AG</span></div>
      <div class="tagline">Digitale Strategien</div>
    </div>

    <div class="address">
      <div>Your company address line 1</div>
      <div class="with-icon">City zipcode line 2
        <svg class="icon" viewBox="0 0 16 16" aria-hidden="true"><circle cx="8" cy="8" r="8"/><path d="M4 8.5 8 4.5l4 4h-1.3V12H9V9.5H7V12H5.3V8.5z" fill="#f3f3f1"/></svg>
      </div>
    </div>

    <div class="person">
      <div class="person-name">YOUR FULL NAME</div>
      <div class="person-title">Your title</div>
      <ul class="contacts">
        <li><svg class="icon" viewBox="0 0 16 16" aria-hidden="true"><circle cx="8" cy="8" r="8"/><path d="M5 4.5c.6-.4 1.2-.3 1.4.2l.6 1.3c.2.4 0 .8-.3 1-.3.2-.3.5-.1.9.5.9 1 1.4 1.8 1.8.4.2.7.2.9-.1.2-.3.6-.5 1-.3l1.3.6c.5.2.6.8.2 1.4-.8 1-2.3 1-4-.2C6 10.1 5 9 4.4 7.6 3.9 6.2 4.1 5.1 5 4.5z" fill="#f3f3f1"/></svg>012-345-6789</li>
        <li><svg class="icon" viewBox="0 0 16 16" aria-hidden="true"><circle cx="8" cy="8" r="8"/><rect x="5.5" y="3.5" width="5" height="9" rx="1" fill="#f3f3f1"/><rect x="6.3" y="4.6" width="3.4" height="5.8" fill="#151515"/></svg>012-345-6789</li>
        <li><svg class="icon" viewBox="0 0 16 16" aria-hidden="true"><circle cx="8" cy="8" r="8"/><rect x="3.8" y="5" width="8.4" height="6" fill="#f3f3f1"/><path d="M3.8 5 8 8.4 12.2 5" fill="none" stroke="#151515" stroke-width=".9"/></svg>your email adress</li>
        <li><svg class="icon" viewBox="0 0 16 16" aria-hidden="true"><circle cx="8" cy="8" r="8"/><g fill="none" stroke="#f3f3f1" stroke-width=".9"><circle cx="8" cy="8" r="4.6"/><ellipse cx="8" cy="8" rx="2" ry="4.6"/><path d="M3.4 8h9.2"/></g></svg>www.yourdomain.com</li>
      </ul>
    </div>
  </section>
</main>
</body>
</html>
```